Tasman Curdworks Guild needs new business cards

We need new business cards designed and produced. We are likely to need other design work done for ads, flyers etc in future.

We would like to start with an initial business card.

The Tasman Curdworks Guild (TCG) is a membership-based not-for-profit organisation that looks after the interests of Australia's small to medium artisan cheesemakers, many of whom are also small-scale farmers. The design should be simple, using our logo, but also communicate our artisan cheese and small dairy farm focus.

The first card to be designed and produced is for me, Miriam Tolhurst. My details are:

Miriam Tolhurst
Secretary
Tasman Curdworks Guild (TCG)
http://www.curdworksguild.example
T +61452837190
E miriam.miriamtolhurst@mailbox.example

I have attached the TCG logo in jpg form. I have a higher resolution version available if needed.

Thank you!

Miriam

Miriam Tolhurst
Tasman Curdworks Guild
miriam.miriamtolhurst@mailbox.example
+61452837190

Sans Serif

• Logo (see attached file)

```html
<!DOCTYPE html>
<html lang="en">
<head>
<meta charset="utf-8">
<title>Tasman Curdworks Guild — Business Card</title>
<link rel="stylesheet" href="https://fonts.googleapis.com/css2?family=Marcellus&family=Sorts+Mill+Goudy&family=Montserrat:wght@600;700&display=swap">
<style>
  :root {
    --backdrop: #ece8e2;
    --card: #ffffff;
    --frame: #f5b53a;
    --name: #e07a3a;
    --title-gold: #f4bd48;
    --ink-brown: #6e4522;
    --flourish: #ec9a6a;
  }
  * { margin: 0; padding: 0; box-sizing: border-box; }
  html, body {
    width: 1200px; height: 1015px; overflow: hidden;
    background: var(--backdrop);
  }
  .card {
    position: absolute; left: 50px; top: 192px;
    width: 1100px; height: 630px;
    background: var(--card);
    border-radius: 44px;
    box-shadow: 0 10px 30px rgba(0,0,0,0.18);
    overflow: hidden;
  }
  .card-frame { position: absolute; left: 0; top: 0; }
  .brand {
    position: absolute; left: 110px; top: 180px;
    display: flex; align-items: center; gap: 24px;
  }
  .brand-dot {
    width: 70px; height: 70px; border-radius: 50%;
    background: var(--frame);
    flex: none;
  }
  .brand-name {
    font-family: "Sorts Mill Goudy", serif;
    font-size: 44px; line-height: 1.05;
    color: var(--ink-brown);
    letter-spacing: 1px;
  }
  .details { position: absolute; left: 560px; top: 130px; width: 470px; }
  .person-name {
    font-family: "Marcellus", serif;
    font-size: 38px; letter-spacing: 3px;
    color: var(--name);
    text-transform: uppercase;
    white-space: nowrap;
    text-align: right;
  }
  .name-flourish {
    display: block; margin: 6px 0 0 230px;
    width: 150px; height: 12px;
    background: var(--flourish); opacity: 0.5;
    border-radius: 6px;
  }
  .role {
    margin-top: 44px;
    font-family: "Montserrat", sans-serif; font-weight: 700;
    color: var(--title-gold);
    font-size: 20px; line-height: 1.3; letter-spacing: 1px;
  }
  .role-org { margin-top: 8px; }
  .contacts {
    list-style: none; margin-top: 62px;
    font-family: "Montserrat", sans-serif; font-weight: 600;
    color: var(--ink-brown); font-size: 17px;
  }
  .contacts li { display: flex; align-items: center; gap: 12px; height: 38px; white-space: nowrap; }
  .contacts svg { flex: none; }
</style>
</head>
<body>
<div class="card">
  <svg class="card-frame" width="1100" height="630" viewBox="0 0 1100 630" aria-hidden="true">
    <path d="M64,40 H1036 A24,24 0 0 0 1060,64 V566 A24,24 0 0 0 1036,590 H64 A24,24 0 0 0 40,566 V64 A24,24 0 0 0 64,40 Z"
          fill="none" stroke="var(--frame)" stroke-width="3"/>
  </svg>

  <div class="brand">
    <span class="brand-dot"></span>
    <div class="brand-name">Tasman<br>Curdworks<br>Guild</div>
  </div>

  <div class="details">
    <div class="person-name">Miriam Tolhurst</div>
    <span class="name-flourish" role="img" aria-label="Small decorative flourish under the name"></span>

    <div class="role">
      <div>Secretary</div>
      <div class="role-org">Tasman Curdworks Guild (TCG)</div>
    </div>

    <ul class="contacts">
      <li>
        <svg width="24" height="24" viewBox="0 0 24 24" aria-hidden="true"><path fill="var(--ink-brown)" d="M6.6 10.8a15.1 15.1 0 0 0 6.6 6.6l2.2-2.2c.3-.3.7-.4 1-.2 1.1.4 2.3.6 3.6.6.6 0 1 .4 1 1V20c0 .6-.4 1-1 1A17 17 0 0 1 3 4c0-.6.4-1 1-1h3.5c.6 0 1 .4 1 1 0 1.3.2 2.5.6 3.6.1.3 0 .7-.2 1z"/></svg>
        <span>miriam.miriamtolhurst@mailbox.example</span>
      </li>
      <li>
        <svg width="24" height="24" viewBox="0 0 24 24" aria-hidden="true"><rect x="2.5" y="5.5" width="19" height="13" fill="none" stroke="var(--ink-brown)" stroke-width="1.6"/><path d="M2.5 5.5 12 13l9.5-7.5M2.5 18.5l7-6M21.5 18.5l-7-6" fill="none" stroke="var(--ink-brown)" stroke-width="1.6"/></svg>
        <span>+61452837190</span>
      </li>
      <li>
        <svg width="24" height="24" viewBox="0 0 24 24" aria-hidden="true"><g fill="none" stroke="var(--ink-brown)" stroke-width="1.5"><circle cx="12" cy="12" r="9.5"/><ellipse cx="12" cy="12" rx="4.2" ry="9.5"/><path d="M2.5 12h19M4 7h16M4 17h16"/></g></svg>
        <span>http://www.curdworksguild.example</span>
      </li>
    </ul>
  </div>
</div>
</body>
</html>
```